Website for New Phone Company

Our company "Lagoonfield Telecom" requires a new web-site.

We enable Pacific Islanders (Fijians, Samoans, Tongans) to speak to their friends and family back home for a fraction of the cost of other phone companies whilst maintaining a quality. Our target audience is price sensitive but is demanding with quality, we would like them to gather a feel that they are dealing with a safe company that is orientated towards the Pacific Island community, has low pricing and yet doesn't compromise on quality.

We are going to be marketing via online channels and so a Google friendly web-site is important. We essentially need three pages designed which we will use with our content.

Page 1 - Homepage Lagoonfield Telecom - Our prime brand is Lagoonfield Telecom and we would like to promote this brand on our web-site.

However, we have three plans under this brand called Miroka, Selavi and Penuko. We would like the main page to have three unique service offerings for Penuko, Selavi and Miroka. Something along the lines of being able to choose a plan down on the page. I would like to give examples here of companies in our industry that are extremely successful in this trade i.e. www.ringvelo.co.nz, www.9speakly.co.nz, www.quorlix.com

The objective of this design is to present the customer with three unique offerings targeted to Samoa (Penuko), Selavi (Tonga) and Miroka (Fiji).

Page 2 - Content/Template Page for Lagoonfield Telecom - We require a page where we can place content like About Us, Contact Us etc.

Page 3 - We require a single design that will fit all three brands as per the brand images attached for Miroka, Penuko and Selavi. This will almost be used as a landing page to brand the plan exclusively under our company. All three plans / service offerings are being marketed under "Lagoonfield Telecom" which makes it important to use both the service offering logo as well as the company logo. This page needs to act more as a promotional page where it promotes our service offering. e.g. Call Samoa from only 50c a minute type of thing.

The objective of the design of the landing / service offering page is to entice the customer to act upon the offer by joining our organisation.

We will be available throughout the process to guide you better.
Updates

Reason: We haven't received suitable designs to choose from. We would like to see quality work not quantity.

Industry/Entity Type

It Company

```html
<!DOCTYPE html>
<html lang="en">
<head>
<meta charset="utf-8">
<title>Lagoonfield Telecom</title>
<link href="https://fonts.googleapis.com/css2?family=Oswald:wght@400;500&family=Open+Sans:wght@400;600;700&display=swap" rel="stylesheet">
<style>
  :root {
    --brand-red: #d21f1b;
    --red-dark: #b8140f;
    --text-dark: #1f1f1f;
    --text-grey: #6b6b6b;
    --muted: #9a9a9a;
    --line: #dcdcdc;
    --band: #f0f0f0;
    --footer: #2a2a2a;
    --navy: #1d3557;
    --miroka: #c0392b;
    --penuko: #a8c21a;
    --selavi: #45a63a;
  }
  * { box-sizing: border-box; margin: 0; padding: 0; }
  html, body { width: 902px; height: 1200px; overflow: hidden; background: #fff; }
  body { position: relative; font-family: "Open Sans", Arial, sans-serif; color: var(--text-dark); }

  .site-header { position: absolute; left: 0; top: 0; width: 902px; height: 67px; border-top: 2px solid var(--brand-red); background: #fff; box-shadow: 0 1px 3px rgba(0,0,0,.12); }
  .brand { position: absolute; left: 133px; top: 10px; display: flex; align-items: center; gap: 10px; }
  .brand-mark { width: 44px; height: 44px; border-radius: 50%; background: var(--brand-red); }
  .brand-name { font-weight: 600; color: #6a6a6a; line-height: 1; }
  .brand-name .line1 { display: block; font-size: 25px; }
  .brand-name .line2 { display: block; font-size: 14px; margin-top: 2px; }

  .social { position: absolute; left: 610px; top: 14px; display: flex; gap: 14px; font-size: 9px; color: #444; align-items: center; }
  .social .dot { display: inline-block; width: 11px; height: 11px; background: #cfcfcf; vertical-align: middle; margin-right: 4px; }
  .social .plus { width: 30px; height: 13px; border: 1px solid #ccc; background: #fafafa; }

  .main-nav { position: absolute; right: 147px; top: 44px; display: flex; gap: 6px; }
  .main-nav a { font-size: 9.5px; font-weight: 600; color: #222; text-decoration: none; padding: 3px 7px; }
  .main-nav a.active { background: var(--brand-red); color: #fff; }

  .hero { position: absolute; left: 0; top: 67px; width: 902px; height: 313px;
    background: linear-gradient(180deg, #3d8fd6 0%, #8cc4ee 30%, #e9f3fb 48%, #1f8fb5 55%, #4fc3c8 63%, #cfe7e6 70%, #f2f1ec 78%, #e6e4de 100%); }

  .plans { position: absolute; left: 109px; top: 401px; display: flex; gap: 21px; }
  .plan-card { width: 207px; height: 290px; border: 1px solid var(--line); background: #fff; box-shadow: 0 1px 3px rgba(0,0,0,.08); text-align: center; font-family: "Oswald", "Arial Narrow", sans-serif; }
  .plan-logo { height: 104px; display: flex; flex-direction: column; align-items: center; justify-content: flex-end; }
  .plan-icon { width: 48px; height: 48px; border-radius: 50%; margin-bottom: 6px; }
  .plan-name { font-size: 24px; font-weight: 500; letter-spacing: .5px; line-height: 1; }
  .plan-validity { margin-top: 14px; font-size: 15px; color: var(--muted); }
  .plan-price { font-size: 36px; font-weight: 500; color: #222; line-height: 1.2; margin-top: 2px; }
  .plan-period { font-size: 15px; color: var(--muted); line-height: 1; }
  .buy-btn { display: block; margin: 20px auto 0; width: 156px; height: 34px; line-height: 34px; border-radius: 3px; background: linear-gradient(180deg, #ee4a3f, var(--red-dark)); color: #fff; font-size: 18px; text-decoration: none; }
  .read-more { display: block; margin-top: 13px; font-size: 16px; color: #222; text-decoration: none; }

  .tagline-band { position: absolute; left: 0; top: 715px; width: 902px; height: 93px; background: var(--band); text-align: center; font-weight: 700; font-size: 14.5px; color: #222; padding-top: 18px; line-height: 27px; }
  .tagline-band em { font-style: normal; color: var(--brand-red); font-size: 21px; }

  .section-title { position: absolute; left: 0; width: 902px; text-align: center; font-size: 16px; color: var(--navy); }
  .divider { position: absolute; height: 1px; background: var(--line); }
  .divider-icon { position: absolute; }

  .news-item { position: absolute; top: 887px; width: 320px; }
  .news-date { position: absolute; left: 0; top: 0; width: 34px; height: 41px; background: #eeeeee; text-align: center; color: #666; }
  .news-date .month { display: block; font-size: 8px; padding-top: 5px; }
  .news-date .day { display: block; font-size: 15px; }
  .news-body { position: absolute; left: 50px; top: 0; width: 270px; }
  .news-title { font-size: 11.5px; font-weight: 700; color: var(--brand-red); }
  .news-text { margin-top: 6px; font-size: 7.5px; line-height: 12px; color: #555; }

  .partners { position: absolute; left: 142px; top: 1073px; display: flex; gap: 10px; }
  .partner-badge { width: 112px; height: 41px; border: 1px solid var(--line); background: #fff; display: flex; align-items: center; justify-content: center; }
  .partner-badge span { width: 70px; height: 18px; background: #c9d4e0; border-radius: 3px; }
  .partner-badge.alt span { background: #e3b7b5; }
  .partner-badge.dark { background: #6f8fa8; border-color: #4e6d85; }
  .partner-badge.dark span { background: #2f6f99; }
  .carousel-arrow { position: absolute; top: 1085px; }

  .site-footer { position: absolute; left: 0; top: 1170px; width: 902px; height: 30px; background: var(--footer); color: #bbb; font-size: 7px; padding: 10px 0 0 108px; }
</style>
</head>
<body>

<header class="site-header">
  <div class="brand">
    <span class="brand-mark"></span>
    <span class="brand-name"><span class="line1">Lagoonfield</span><span class="line2">Telecom</span></span>
  </div>
  <div class="social">
    <span><span class="dot plus"></span></span>
    <span><span class="dot"></span>Join us</span>
    <span><span class="dot"></span>Follow us</span>
  </div>
  <nav class="main-nav">
    <a class="active" href="#">HOME</a>
    <a href="#">PHONECARDS</a>
    <a href="#">RECHARGE</a>
    <a href="#">PRODUCTS</a>
    <a href="#">ABOUT US</a>
    <a href="#">CONTACT</a>
  </nav>
</header>

<div class="hero" role="img" aria-label="Couple holding hands on a white sand beach under a palm tree, looking at a turquoise sea and blue sky"></div>

<section class="plans">
  <article class="plan-card">
    <div class="plan-logo"><span class="plan-icon" style="background:var(--miroka)"></span><span class="plan-name" style="color:var(--miroka)">MIROKA</span></div>
    <p class="plan-validity">valid for 1 year</p>
    <p class="plan-price">$7.79</p>
    <p class="plan-period">per month</p>
    <a class="buy-btn" href="#">Buy Now</a>
    <a class="read-more" href="#">read more</a>
  </article>
  <article class="plan-card">
    <div class="plan-logo"><span class="plan-icon" style="background:#f2c200"></span><span class="plan-name" style="color:var(--penuko)">Penuko</span></div>
    <p class="plan-validity">valid for 1 year</p>
    <p class="plan-price">$9.79</p>
    <p class="plan-period">per month</p>
    <a class="buy-btn" href="#">Buy Now</a>
    <a class="read-more" href="#">read more</a>
  </article>
  <article class="plan-card">
    <div class="plan-logo"><span class="plan-icon" style="background:var(--selavi)"></span><span class="plan-name" style="color:var(--selavi)">Selavi</span></div>
    <p class="plan-validity">valid for 1 year</p>
    <p class="plan-price">$11.79</p>
    <p class="plan-period">per month</p>
    <a class="buy-btn" href="#">Buy Now</a>
    <a class="read-more" href="#">read more</a>
  </article>
</section>

<section class="tagline-band">
  <p>Doesn’t matter <em>wherever</em> you are, just get connected using our <em>economical</em></p>
  <p>services without compromising on <em>quality</em> of voice.</p>
</section>

<h2 class="section-title" style="top:825px">In the Spotlight</h2>
<div class="divider" style="left:360px; top:865px; width:182px"></div>
<svg class="divider-icon" style="left:440px; top:859px" width="12" height="12" viewBox="0 0 12 12"><path d="M6 10.5 1.5 6a2.6 2.6 0 0 1 4.5-2.6A2.6 2.6 0 0 1 10.5 6Z" fill="#fff" stroke="#ccc"/></svg>

<article class="news-item" style="left:112px">
  <div class="news-date"><span class="month">SEP</span><span class="day">14</span></div>
  <div class="news-body">
    <h3 class="news-title">Voluptatem accusantium</h3>
    <p class="news-text">Calling home to Suva, Apia or Nuku'alofa now costs less than ever. Our new plans bring clear voice lines to every island family, with simple monthly prices, no hidden fees and friendly support from people who know the Pacific community well.</p>
  </div>
</article>
<article class="news-item" style="left:449px">
  <div class="news-date"><span class="month">SEP</span><span class="day">12</span></div>
  <div class="news-body">
    <h3 class="news-title">Voluptatem accusantium</h3>
    <p class="news-text">We have upgraded our network partners to give every call a cleaner sound. Customers on all three plans will notice faster connections and fewer dropped calls, while the price they pay each month stays exactly the same as before.</p>
  </div>
</article>

<div class="divider" style="left:109px; top:1002px; width:663px"></div>
<svg class="divider-icon" style="left:443px; top:998px" width="10" height="8" viewBox="0 0 10 8"><path d="M1 1l4 5 4-5" fill="none" stroke="#bbb" stroke-width="1.5"/></svg>

<h2 class="section-title" style="top:1027px">Our Partners</h2>
<svg class="carousel-arrow" style="left:117px" width="10" height="16" viewBox="0 0 10 16"><path d="M8 2 2 8l6 6" fill="none" stroke="#bbb" stroke-width="2"/></svg>
<div class="partners">
  <div class="partner-badge"><span></span></div>
  <div class="partner-badge alt"><span></span></div>
  <div class="partner-badge dark"><span></span></div>
  <div class="partner-badge"><span></span></div>
  <div class="partner-badge alt"><span></span></div>
</div>
<svg class="carousel-arrow" style="left:753px" width="10" height="16" viewBox="0 0 10 16"><path d="M2 2l6 6-6 6" fill="none" stroke="#999" stroke-width="2"/></svg>

<footer class="site-footer">Copyright 2014 Lagoonfield Telecom, All rights reserved.</footer>

</body>
</html>
```